Wordpress Design for my Consulting Company

We want a WordPress site created for our new business. We have created a mock-up of the content we want on the site at https://marcusdellow.example-sites.com/website-5

We are not attached to any of the pictures and just put stock stuff from wix's editor, which we don't have rights to use outside of wix.

We are NOT looking to just port this site to WordPress, we are looking for some creative ways to display the content in a more professional artistic sense.

I have included several logo files and a text file with the colors and Fonts used in the logo. We are not looking to change the logo or the colors used in the logo.

The Schedule appointment links to a page that embeds a bookingnest.example.com calendar. https://bookingnest.example.com/marcus-dellow/brightvale

The final website domain will be enterprisebrightvale.example

Enterprise brightvale is a consulting company that works directly with the business owners and leaders of small businesses between 50-200 employees. We help companies make sure they have the right technology to meet their strategic goals. We are the anti-"Computer Guy" and we focus on business outcomes NOT cool technology gadgets.

The final design should communicate business growth and success.

Target Market(s)

Business Owners of companies with 50-200 employees

Coding

Coded - Design and coding required

Number of Pages Required

1 page

Font styles to use
Serif
Other font styles liked:
• Trajan Pro Bold, Open Sans

Requirements
Must have
• Should focus on consulting rather than technology.
• Should show the customer as the hero and we are just their guide.
• Must use the logo provided and the colors and fonts in the text file provided. Any other colors and fonts must be complementary.
• The design should scale for all devices computer, iPad, or phone
Should not have
• Should not focus on technology, we are the anti-"Computer Guy" and we focus on business outcomes NOT cool technology gadgets.

```html
<!DOCTYPE html>
<html lang="en">
<head>
<meta charset="utf-8">
<title>Brightvale — They say</title>
<link rel="stylesheet" href="https://fonts.googleapis.com/css2?family=Poppins:wght@500;600;700&family=Rubik:wght@400;500&display=swap">
<style>
  :root {
    --sidebar-bg: #ffffff;
    --ink-dark: #2b2b2b;
    --testimonial-bg: #3c4a52;
    --newsletter-bg: #333333;
    --white: #ffffff;
    --muted: #8d979d;
    --muted-dark: #4d4d4d;
    --field-line: #6a6a6a;
    --arrow-bg: #2b3135;
    --accent-ring: #8b5a3c;
    --photo-a: #c9c3bd;
    --photo-b: #8c7a6c;
    --photo-c: #6f6a66;
  }
  * { box-sizing: border-box; margin: 0; padding: 0; }
  html, body { width: 1200px; height: 608px; overflow: hidden; background: var(--sidebar-bg); }
  body { position: relative; font-family: "Rubik", sans-serif; }

  .sidebar { position: absolute; left: 0; top: 0; width: 64px; height: 608px; background: var(--sidebar-bg); }
  .menu-toggle { position: absolute; left: 24px; top: 21px; }
  .sidebar-copyright {
    position: absolute; left: 32px; top: 260px;
    transform: translate(-50%, -50%) rotate(-90deg);
    white-space: nowrap; font-family: "Poppins", sans-serif; font-weight: 500;
    font-size: 8.5px; letter-spacing: 0.4px; color: var(--ink-dark);
  }
  .sidebar-rule { position: absolute; left: 31px; top: 323px; width: 1px; height: 50px; background: #d6d6d6; }
  .sidebar-rule::before { content: ""; position: absolute; left: -0.5px; top: 0; width: 2px; height: 25px; background: var(--ink-dark); }

  .hero-photo {
    position: absolute; left: 64px; top: 0; width: 1136px; height: 66px;
    background: linear-gradient(90deg, var(--photo-a) 0%, var(--photo-b) 35%, var(--photo-c) 55%, var(--photo-a) 75%, var(--photo-c) 100%);
    opacity: 0.85;
  }

  .testimonials { position: absolute; left: 64px; top: 66px; width: 1136px; height: 417px; background: var(--testimonial-bg); color: var(--white); }
  .section-kicker { position: absolute; left: 0; width: 100%; top: 80px; text-align: center; font-family: "Poppins", sans-serif; font-weight: 600; font-size: 12px; }
  .section-title { position: absolute; left: 0; width: 100%; top: 100px; text-align: center; font-family: "Poppins", sans-serif; font-weight: 600; font-size: 32px; letter-spacing: -0.5px; }

  .quote { position: absolute; top: 168px; width: 480px; }
  .quote--first { left: 72px; }
  .quote--second { left: 580px; }
  .quote-text { font-size: 13.5px; line-height: 24.3px; }
  .quote--first .quote-text { font-weight: 500; }
  .quote-author { margin-top: 6px; font-family: "Poppins", sans-serif; font-weight: 600; font-size: 14px; letter-spacing: -0.2px; }
  .quote-company { margin-top: 2px; font-family: "Poppins", sans-serif; font-weight: 500; font-size: 12px; color: var(--muted); letter-spacing: -0.2px; }

  .slider-arrow { position: absolute; top: 190px; }
  .slider-arrow--prev { left: -8px; }
  .slider-arrow--next { left: 1100px; }
  .slider-dots { position: absolute; left: 550px; top: 325px; }

  .newsletter { position: absolute; left: 64px; top: 483px; width: 1136px; height: 125px; background: var(--newsletter-bg); }
  .newsletter-title { position: absolute; left: 65px; top: 39px; font-family: "Poppins", sans-serif; font-weight: 600; font-size: 18.5px; color: var(--white); letter-spacing: -0.3px; }
  .newsletter-note { position: absolute; left: 65px; top: 67px; font-family: "Poppins", sans-serif; font-size: 11px; color: var(--muted-dark); }
  .newsletter-field { position: absolute; left: 495px; top: 60px; width: 575px; height: 54px; border-bottom: 1px solid var(--field-line); }
  .newsletter-field label { font-size: 11px; color: var(--muted-dark); }
  .back-to-top { position: absolute; left: 1069px; top: 58px; }
</style>
</head>
<body>
  <aside class="sidebar">
    <svg class="menu-toggle" width="16" height="13" viewBox="0 0 16 13" aria-label="Menu">
      <rect y="0" width="16" height="1.6" fill="#2b2b2b"/>
      <rect y="5.5" width="16" height="1.6" fill="#2b2b2b"/>
      <rect y="11" width="16" height="1.6" fill="#2b2b2b"/>
    </svg>
    <div class="sidebar-copyright">© 2018, BRIGHTVALE</div>
    <div class="sidebar-rule"></div>
  </aside>

  <div class="hero-photo" role="img" aria-label="Photo of a team meeting in a bright office, cropped"></div>

  <section class="testimonials">
    <p class="section-kicker">Quickly unleash</p>
    <h2 class="section-title">They say</h2>

    <blockquote class="quote quote--first">
      <p class="quote-text">``The team at Brightvale has been instrumental in helping us grow from one location to six, and has positioned us with a competitive advantage through our use of technology.``</p>
      <p class="quote-author">— Dale Merriton</p>
      <p class="quote-company">Lend-A-Lot</p>
    </blockquote>

    <blockquote class="quote quote--second">
      <p class="quote-text">“Owen and the team at Brightvale have been a valuable asset in overseeing technology alignment from a leadership level, and have turned technology into a tool to support and enable growth, rather than hinder it.``</p>
      <p class="quote-author">— Reed Callway Pastor</p>
      <p class="quote-company">Operations and Leadership Development Harbor Hill Church</p>
    </blockquote>

    <svg class="slider-arrow slider-arrow--prev" width="44" height="44" viewBox="0 0 44 44" aria-label="Previous">
      <circle cx="22" cy="22" r="21" fill="var(--arrow-bg)"/>
      <path d="M14 22h16M14 22l5-5M14 22l5 5" stroke="#fff" stroke-width="1.3" fill="none"/>
    </svg>
    <svg class="slider-arrow slider-arrow--next" width="44" height="44" viewBox="0 0 44 44" aria-label="Next">
      <circle cx="22" cy="22" r="21" fill="var(--arrow-bg)"/>
      <path d="M14 22h16M30 22l-5-5M30 22l-5 5" stroke="#fff" stroke-width="1.3" fill="none"/>
    </svg>

    <svg class="slider-dots" width="36" height="14" viewBox="0 0 36 14" aria-label="Slide 1 of 2">
      <circle cx="8" cy="7" r="5.2" fill="none" stroke="#fff" stroke-width="1.1"/>
      <circle cx="8" cy="7" r="1.6" fill="#fff"/>
      <circle cx="28" cy="7" r="1.6" fill="#fff"/>
    </svg>
  </section>

  <section class="newsletter">
    <h3 class="newsletter-title">Join the design tribe newsletter</h3>
    <p class="newsletter-note">We respect your privacy, so we never share your info</p>
    <div class="newsletter-field"><label>Your Name (required)</label></div>
    <svg class="back-to-top" width="44" height="44" viewBox="0 0 44 44" aria-label="Back to top">
      <circle cx="22" cy="22" r="20.5" fill="none" stroke="var(--accent-ring)" stroke-width="1"/>
      <path d="M22 30V14M22 14l-4 4M22 14l4 4" stroke="#9a9a9a" stroke-width="1" fill="none"/>
    </svg>
  </section>
</body>
</html>
```